BOLD & MINIMALIST DESIGN NEEDED

We want a very bold but minimalistic business card design that is impactful and utilizes both sides of the business card. Our current logo is included for your use.

We want bold fonts and good use of negative space. We don't want the logo to overpower the design.

Target Market(s)

Professionals who are building new commercial buildings.

Industry/Entity Type

Construction

Contact Information for Business Card

Name, Title, email, office phone, cell phone, website

Font styles to use
Serif
Sans Serif

Requirements
Must have
• Bold design!

```html
<!DOCTYPE html>
<html lang="en">
<head>
<meta charset="utf-8">
<title>Ridgecrest Business Card</title>
<link href="https://fonts.googleapis.com/css2?family=Arimo:wght@400;700&display=swap" rel="stylesheet">
<style>
  :root {
    --page-bg: #e4e4e4;
    --card-bg: #ffffff;
    --ink: #111111;
    --ink-soft: #444444;
    --accent: #7dc242;
    --rule: #4a5560;
  }
  * { box-sizing: border-box; margin: 0; padding: 0; }
  html, body {
    width: 1200px;
    height: 1200px;
    overflow: hidden;
    background: var(--page-bg);
    font-family: "Arimo", Arial, sans-serif;
  }
  .canvas {
    position: relative;
    width: 1200px;
    height: 1200px;
  }
  .card {
    position: absolute;
    left: 255px;
    width: 690px;
    height: 394px;
    background: var(--card-bg);
  }
  .card--front { top: 160px; }
  .card--back { top: 650px; }

  .identity {
    position: absolute;
    right: 367px;
    top: 170px;
    text-align: right;
  }
  .identity__name {
    font-weight: 700;
    font-size: 27px;
    color: var(--ink);
    letter-spacing: 0.5px;
    line-height: 1;
  }
  .identity__title {
    margin-top: 8px;
    font-size: 16px;
    color: var(--accent);
  }
  .divider {
    position: absolute;
    left: 340px;
    top: 156px;
    width: 1.5px;
    height: 81px;
    background: var(--rule);
  }
  .contacts {
    position: absolute;
    left: 360px;
    top: 155px;
    list-style: none;
  }
  .contacts__item {
    display: flex;
    align-items: center;
    height: 20.7px;
    font-size: 16.5px;
    color: var(--ink-soft);
  }
  .contacts__icon {
    width: 14px;
    height: 14px;
    margin-right: 9px;
    fill: var(--ink);
    flex: none;
  }

  .wordmark {
    position: absolute;
    left: 0;
    right: 0;
    top: 180px;
    display: flex;
    justify-content: center;
    align-items: center;
    gap: 16px;
  }
  .wordmark__square {
    width: 34px;
    height: 34px;
    background: var(--accent);
  }
  .wordmark__name {
    font-weight: 700;
    font-size: 52px;
    letter-spacing: 1px;
    color: var(--ink);
    line-height: 1;
  }
</style>
</head>
<body>
<main class="canvas">
  <section class="card card--front" aria-label="Card front">
    <div class="identity">
      <p class="identity__name">DANIEL REYES</p>
      <p class="identity__title">President</p>
    </div>
    <div class="divider"></div>
    <ul class="contacts">
      <li class="contacts__item">
        <svg class="contacts__icon" viewBox="0 0 24 24" aria-hidden="true"><path d="M6.6 10.8a15.1 15.1 0 0 0 6.6 6.6l2.2-2.2a1 1 0 0 1 1-.25 11.4 11.4 0 0 0 3.6.57 1 1 0 0 1 1 1V20a1 1 0 0 1-1 1A17 17 0 0 1 3 4a1 1 0 0 1 1-1h3.5a1 1 0 0 1 1 1c0 1.25.2 2.46.57 3.6a1 1 0 0 1-.25 1z"/></svg>
        555-210-4817
      </li>
      <li class="contacts__item">
        <svg class="contacts__icon" viewBox="0 0 24 24" aria-hidden="true"><path d="M7 1h10a2 2 0 0 1 2 2v18a2 2 0 0 1-2 2H7a2 2 0 0 1-2-2V3a2 2 0 0 1 2-2zm0 3v14h10V4zm5 15.5a1 1 0 1 0 0 2 1 1 0 0 0 0-2z"/></svg>
        555-392-7064
      </li>
      <li class="contacts__item">
        <svg class="contacts__icon" viewBox="0 0 24 24" aria-hidden="true"><path d="M2 5h20v14H2zm2 2v.4l8 5 8-5V7zm0 2.8V17h16V9.8l-8 5z"/></svg>
        info@ridgecrest.com
      </li>
      <li class="contacts__item">
        <svg class="contacts__icon" viewBox="0 0 24 24" aria-hidden="true"><path d="M12 2a10 10 0 1 0 0 20 10 10 0 0 0 0-20zm-1 17.9A8 8 0 0 1 4.2 10.6L9 15.4v1a2 2 0 0 0 2 2zm6.9-2.5A2 2 0 0 0 16 16h-1v-3a1 1 0 0 0-1-1H8v-2h2a1 1 0 0 0 1-1V7h2a2 2 0 0 0 2-2v-.4a8 8 0 0 1 2.9 12.8z"/></svg>
        www.ridgecrest.com
      </li>
    </ul>
  </section>

  <section class="card card--back" aria-label="Card back">
    <div class="wordmark">
      <span class="wordmark__square" aria-hidden="true"></span>
      <span class="wordmark__name">RIDGECREST</span>
    </div>
  </section>
</main>
</body>
</html>
```